New Look and Feel for 82 year old Varnstedt Ltd. presentations

We are seeking new ideas to have powerpoint-layouts for the group headquarters. Varnstedt is an industrial company in maritime, hydraulics, heavy machinery and industrial services. Please read our history and watch the video for a quick familiarization. http://www.varnstedt-example.fi/eng/main.php

Our customer relationships are based on trust, with Varnstedt providing to customers, cooperation partners and other interest groups products and solutions that produce sustainable benefits.

Varnstedt strives to ensure that the environmental impact of the products is considered over the entire life cycle and the processes used by the Group are as environmentally benign as possible.

Colors

Designer to choose colors to be used in the design.

Requirements
Must have
• Logo
Nice to have
• example animations and transitions

```html
<!DOCTYPE html>
<html lang="en">
<head>
<meta charset="utf-8">
<title>Varnstedt Ltd. presentation layouts</title>
<link rel="stylesheet" href="https://fonts.googleapis.com/css2?family=Oswald:wght@400;500;600&family=Roboto:wght@400;500&family=Open+Sans:wght@400;600&display=swap">
<style>
  :root {
    --red: #c8202a;
    --red-bright: #e23b40;
    --red-deep: #a70f17;
    --red-dark: #8e1318;
    --ink: #35353b;
    --ink-soft: #5a5a5a;
    --paper: #ececec;
    --paper-light: #f7f7f7;
    --text: #222;
    --white: #fff;
  }
  * { margin: 0; padding: 0; box-sizing: border-box; }
  html, body { width: 1061px; height: 1200px; overflow: hidden; background: var(--white); }
  body { position: relative; font-family: "Roboto", Arial, sans-serif; color: var(--text); }

  .slide {
    position: absolute; width: 589px; height: 441px; overflow: hidden;
    transform: scale(0.8014); transform-origin: 0 0;
    box-shadow: 0 1px 4px rgba(0,0,0,.35);
  }
  .slide-label {
    position: absolute; width: 472px; text-align: center;
    font-family: "Open Sans", Arial, sans-serif; font-size: 21px; color: #333;
  }
  .abs { position: absolute; }
  .head { font-family: "Oswald", sans-serif; text-transform: uppercase; line-height: 1.05; }
  .accent { color: var(--red); }

  /* cover */
  .cover { background: linear-gradient(160deg, var(--paper-light), #dcdcdc); }
  .cover svg.shapes { position: absolute; inset: 0; }
  .brand { font-family: "Oswald", sans-serif; font-weight: 600; letter-spacing: .5px; display: flex; align-items: center; gap: 10px; }
  .brand-mark { display: inline-block; background: var(--red); }
  .cover .brand { left: 232px; top: 18px; font-size: 34px; color: var(--ink); }
  .cover .brand-mark { width: 26px; height: 26px; }
  .cover-kicker { left: 23px; top: 188px; color: var(--white); font-size: 17px; font-weight: 500; }
  .cover-kicker-text { left: 23px; top: 212px; width: 155px; color: #ddd; font-size: 7.5px; line-height: 1.35; }
  .cover-title { left: 22px; top: 318px; font-size: 29px; font-weight: 500; color: var(--text); }
  .cover-strap { left: 15px; top: 383px; background: #111; color: var(--white); font-family: "Oswald", sans-serif; font-size: 14px; padding: 1px 8px; }
  .cover-web { right: 24px; top: 404px; color: var(--white); font-size: 9px; font-weight: 500; display: flex; align-items: center; gap: 6px; }
  .cover-web::before { content: ""; width: 110px; height: 1px; background: #888; margin-right: 8px; }
  .globe { width: 11px; height: 11px; }

  /* back */
  .back { background: linear-gradient(160deg, var(--paper-light), #dcdcdc); }
  .back-top { left: 0; top: 0; width: 589px; height: 138px; background: var(--red-deep); }
  .back .brand { left: 0; top: 44px; width: 589px; justify-content: center; font-size: 38px; color: var(--white); }
  .back .brand-mark { width: 26px; height: 26px; background: var(--white); }
  .back-mid { left: 0; top: 138px; width: 589px; height: 150px; background: var(--ink); text-align: center; }
  .back-mid .head { font-size: 22px; color: var(--white); margin-top: 30px; }
  .back-mid .head .accent { color: #e8454a; }
  .back-rule { width: 40px; height: 1px; background: #aaa; margin: 7px auto 10px; }
  .back-mid p { color: #ddd; font-size: 7.5px; line-height: 1.4; width: 300px; margin: 0 auto; }
  .back-contact { left: 0; top: 305px; width: 589px; text-align: center; }
  .back-contact .head { font-size: 22px; color: var(--text); }
  .back-contact p { font-size: 9px; margin-top: 8px; color: #333; line-height: 1.9; }
  .pin { width: 8px; height: 8px; vertical-align: -1px; }
  .back-web { left: 0; top: 406px; width: 589px; display: flex; justify-content: center; align-items: center; gap: 10px; font-size: 9px; font-weight: 500; }
  .back-web::before, .back-web::after { content: ""; width: 110px; height: 1px; background: #777; }

  /* inner pages */
  .page { background: var(--ink); }
  .panel { position: absolute; left: 23px; top: 23px; width: 543px; height: 372px; background: linear-gradient(135deg, #fff, #e2e2e2); }
  .page-foot { position: absolute; left: 0; top: 406px; width: 589px; display: flex; justify-content: center; align-items: center; gap: 10px; color: var(--white); font-size: 8.5px; font-weight: 500; }
  .page-foot::before, .page-foot::after { content: ""; width: 115px; height: 1px; background: #888; }
  .page-num { position: absolute; right: 24px; top: 407px; color: var(--white); font-size: 8px; font-weight: 500; }
  .title { position: absolute; left: 18px; top: 20px; border-left: 2px solid var(--ink); padding-left: 8px; }
  .title .main { font-size: 30px; font-weight: 500; color: var(--text); }
  .title .sub { font-size: 16px; color: var(--red); }
  .body-text { font-size: 7.6px; line-height: 1.72; color: #333; text-align: justify; }
  .photo { position: absolute; }

  /* page 3 */
  .stat-label { position: absolute; width: 90px; }
  .stat-label .head { font-size: 8.5px; font-weight: 500; }
  .stat-label p { font-size: 6.8px; line-height: 1.3; margin-top: 4px; color: #333; }
  .stat-num { font-family: "Roboto", sans-serif; font-weight: 500; font-size: 17px; fill: var(--text); }

  /* page 4 */
  .step { position: absolute; left: 324px; width: 178px; }
  .step .head { font-size: 9px; font-weight: 500; }
  .step p { font-size: 6.8px; line-height: 1.38; margin-top: 2px; color: #333; text-align: justify; }
</style>
</head>
<body>

<!-- Cover -->
<section class="slide cover" style="left:38px; top:20px;">
  <svg class="shapes" viewBox="0 0 589 441" width="589" height="441">
    <polygon points="0,0 60,0 162,98 589,98 589,138 0,138" fill="#b5121b"/>
    <rect x="0" y="138" width="589" height="150" fill="var(--ink)"/>
    <polygon points="198,138 589,138 589,332 398,332" fill="#5a3320" role="img" aria-label="Photo: welder grinding a large steel ring with bright sparks"/>
    <polygon points="310,332 589,332 589,441 370,441" fill="var(--ink)"/>
    <polygon points="0,288 255,288 340,390 0,390" fill="none"/>
    <polygon points="258,292 305,292 345,390 300,390" fill="#b5121b"/>
    <polygon points="58,0 110,0 330,330 280,330" fill="var(--red-bright)"/>
  </svg>
  <div class="abs brand"><span class="brand-mark"></span>Varnstedt</div>
  <div class="abs head cover-kicker">Engineering Works</div>
  <div class="abs cover-kicker-text">Varnstedt Works is a business group which provides turnkey services of the mechanical engineering industry.</div>
  <div class="abs head cover-title">Lorem Ipsum is<br>Simply <span class="accent">Dummy Text</span></div>
  <div class="abs cover-strap">2018 LOREM IPSUM IS SIMPLY DUMMY</div>
  <div class="abs cover-web">
    <svg class="globe" viewBox="0 0 12 12"><circle cx="6" cy="6" r="5.3" fill="none" stroke="#fff" stroke-width="1"/><ellipse cx="6" cy="6" rx="2.3" ry="5.3" fill="none" stroke="#fff" stroke-width=".8"/><line x1=".7" y1="6" x2="11.3" y2="6" stroke="#fff" stroke-width=".8"/></svg>
    www.varnstedt-example.fi
  </div>
</section>
<div class="slide-label" style="left:38px; top:378px;">cover</div>

<!-- Back -->
<section class="slide back" style="left:551px; top:20px;">
  <div class="abs back-top"></div>
  <div class="abs brand"><span class="brand-mark"></span>Varnstedt</div>
  <div class="abs back-mid">
    <div class="head">Lorem Ipsum is<br><span class="accent">Lorem Ipsum is Simply</span></div>
    <div class="back-rule"></div>
    <p>Lorem Ipsum is simply dummy text of the printing and typesetting industry. Lorem Ipsum has been the industry's standard dummy text ever since the 1500s</p>
  </div>
  <div class="abs back-contact">
    <div class="head"><span class="accent">Call us today</span> 020 555 0142</div>
    <p><svg class="pin" viewBox="0 0 10 10"><circle cx="5" cy="5" r="4.5" fill="#333"/><circle cx="5" cy="4.3" r="1.6" fill="#fff"/></svg> Varnstedt Oy, Satamakatu 27, PL 8<br>FI-00990 PORTKAARI</p>
  </div>
  <div class="abs back-web">www.varnstedt-example.fi</div>
</section>
<div class="slide-label" style="left:551px; top:378px;">back</div>

<!-- Page 1 -->
<section class="slide page" style="left:38px; top:412px;">
  <div class="panel">
    <div class="title head"><div class="main">Lorem Ipsum</div><div class="sub">Lorem Ipsum is Simply</div></div>
    <p class="abs body-text" style="left:18px; top:88px; width:236px;">Lorem Ipsum is simply dummy text of the printing and typesetting industry. Lorem Ipsum has been the industry's standard dummy text ever since the 1500s, when an unknown printer took a galley of type and scrambled it to make a type specimen book. It has survive. It has survived not only five centuries, but also the leap into electronic typesetting, remaining essentially unchanged. It was popularised in the 1960s.</p>
    <p class="abs body-text" style="left:284px; top:88px; width:236px;">Lorem Ipsum is simply dummy text of the printing and typesetting industry. Lorem Ipsum has been the industry's standard dummy text ever since the 1500s, when an unknown printer took a galley of type and scrambled it to make a type specimen book. It has survive. It has survived not only five centuries, but also the leap into electronic typesetting, remaining essentially unchanged. It was popularised in the 1960s.</p>
    <div class="photo" role="img" aria-label="Photo: colleagues working together at computer screens in an office" style="left:75px; top:201px; width:394px; height:155px; border:4px solid #cfcfcf; background:linear-gradient(90deg,#3a3530,#4e5a70 55%,#9aa6bd);"></div>
  </div>
  <div class="page-foot">www.varnstedt-example.fi</div>
  <div class="page-num">01</div>
</section>
<div class="slide-label" style="left:38px; top:766px;">page 1</div>

<!-- Page 2 -->
<section class="slide page" style="left:551px; top:412px;">
  <div class="panel">
    <div class="title head"><div class="main">Lorem Ipsum</div><div class="sub">Lorem Ipsum is Simply</div></div>
    <p class="abs body-text" style="left:16px; top:84px; width:512px;">Lorem Ipsum is simply dummy text of the printing and typesetting industry. Lorem Ipsum has been the industry's standard dummy text ever since the 1500s, when an unknown printer took a galley of type and scrambled it to make a type specimen book. It has survive. It has survived not only five centuries, but also the leap into electronic typesetting, remaining essentially unchanged. It was popularised in the 1960s with the release of Letraset sheets containing Lorem Ipsum passages, and more recently with desktop publishing.</p>
    <svg class="abs" style="left:100px; top:150px;" width="350" height="210" viewBox="0 0 350 210">
      <g font-family="Roboto, sans-serif" font-size="4" fill="#444">
        <text x="4" y="201">0</text><text x="4" y="163">1</text><text x="4" y="125">2</text><text x="4" y="87">3</text><text x="4" y="49">4</text><text x="4" y="11">5</text>
      </g>
      <line x1="10" y1="8" x2="10" y2="198" stroke="#999" stroke-width=".6"/>
      <line x1="10" y1="198" x2="340" y2="198" stroke="#999" stroke-width=".6"/>
      <g>
        <rect x="27" y="35" width="16" height="163" fill="var(--red)"/><rect x="47" y="111" width="16" height="87" fill="var(--red-dark)"/><rect x="67" y="122" width="16" height="76" fill="var(--ink-soft)"/>
        <rect x="110" y="103" width="16" height="95" fill="var(--red)"/><rect x="130" y="29" width="16" height="169" fill="var(--red-dark)"/><rect x="150" y="122" width="16" height="76" fill="var(--ink-soft)"/>
        <rect x="193" y="65" width="16" height="133" fill="var(--red)"/><rect x="213" y="130" width="16" height="68" fill="var(--red-dark)"/><rect x="233" y="84" width="16" height="114" fill="var(--ink-soft)"/>
        <rect x="276" y="26" width="16" height="172" fill="var(--red)"/><rect x="296" y="92" width="16" height="106" fill="var(--red-dark)"/><rect x="316" y="8" width="16" height="190" fill="var(--ink-soft)"/>
      </g>
      <g font-family="Roboto, sans-serif" font-size="4" fill="#444" text-anchor="middle">
        <text x="55" y="205">CATEGORY 1</text><text x="138" y="205">CATEGORY 2</text><text x="221" y="205">CATEGORY 3</text><text x="304" y="205">CATEGORY 4</text>
      </g>
    </svg>
  </div>
  <div class="page-foot">www.varnstedt-example.fi</div>
  <div class="page-num">02</div>
</section>
<div class="slide-label" style="left:551px; top:766px;">page 2</div>

<!-- Page 3 -->
<section class="slide page" style="left:38px; top:803px;">
  <div class="panel">
    <div class="title head"><div class="main">Lorem Ipsum</div><div class="sub">Lorem Ipsum is Simply</div></div>
    <svg class="abs" style="left:0; top:0;" width="543" height="372" viewBox="0 0 543 372">
      <line x1="275" y1="95" x2="275" y2="292" stroke="#e3b0b3" stroke-width="1"/>
      <g fill="none" stroke-width="6">
        <circle cx="68" cy="135" r="36" fill="#ececec" stroke="#fff"/>
        <circle cx="68" cy="135" r="36" stroke="var(--red)" stroke-dasharray="113.1 226.2" transform="rotate(180 68 135)"/>
        <circle cx="385" cy="135" r="36" fill="#ececec" stroke="#fff"/>
        <circle cx="385" cy="135" r="36" stroke="var(--red-dark)" stroke-dasharray="158.3 226.2" transform="rotate(-90 385 135)"/>
        <circle cx="68" cy="252" r="36" fill="#ececec" stroke="#fff"/>
        <circle cx="68" cy="252" r="36" stroke="var(--ink-soft)" stroke-dasharray="67.9 226.2" transform="rotate(180 68 252)"/>
        <circle cx="385" cy="252" r="36" fill="#ececec" stroke="#fff"/>
        <circle cx="385" cy="252" r="36" stroke="#111" stroke-dasharray="40 226.2" transform="rotate(180 385 252)"/>
      </g>
      <text class="stat-num" x="68" y="141" text-anchor="middle">50</text>
      <text class="stat-num" x="385" y="141" text-anchor="middle">70</text>
      <text class="stat-num" x="68" y="258" text-anchor="middle">30</text>
      <text class="stat-num" x="385" y="258" text-anchor="middle">10</text>
    </svg>
    <div class="stat-label" style="left:117px; top:116px;"><div class="head">Lorem Ipsum Simply</div><p>Lorem Ipsum is simply dummy text of the printing and typesetting industry.</p></div>
    <div class="stat-label" style="left:434px; top:116px;"><div class="head">Lorem Ipsum Simply</div><p>Lorem Ipsum is simply dummy text of the printing and typesetting industry.</p></div>
    <div class="stat-label" style="left:117px; top:233px;"><div class="head">Lorem Ipsum Simply</div><p>Lorem Ipsum is simply dummy text of the printing and typesetting industry.</p></div>
    <div class="stat-label" style="left:434px; top:233px;"><div class="head">Lorem Ipsum Simply</div><p>Lorem Ipsum is simply dummy text of the printing and typesetting industry.</p></div>
    <p class="abs body-text" style="left:16px; top:319px; width:512px;">Lorem Ipsum is simply dummy text of the printing and typesetting industry. Lorem Ipsum has been the industry's standard dummy text ever since the 1500s, when an unknown printer took a galley of type and scrambled it to make a type specimen book. It has survive. It has survived not only five centuries, but also the leap into electronic typesetting, remaining essentially unchanged.</p>
  </div>
  <div class="page-foot">www.varnstedt-example.fi</div>
  <div class="page-num">03</div>
</section>
<div class="slide-label" style="left:38px; top:1157px;">page 3</div>

<!-- Page 4 -->
<section class="slide page" style="left:551px; top:803px;">
  <div class="panel">
    <div class="title head"><div class="main">Lorem Ipsum</div><div class="sub">Lorem Ipsum is Simply</div></div>
    <div class="photo" role="img" aria-label="Photo: hands holding an open business newspaper over a café table" style="left:0; top:85px; width:258px; height:275px; border:5px solid #c8c8c8; background:linear-gradient(135deg,#4a3a2c,#8c8a86 50%,#3a3632);"></div>
    <svg class="abs" style="left:270px; top:80px;" width="50" height="280" viewBox="0 0 50 280">
      <line x1="24" y1="20" x2="24" y2="256" stroke="#333" stroke-width="1"/>
      <g fill="var(--red)">
        <circle cx="24" cy="26" r="20"/><circle cx="24" cy="102" r="20"/><circle cx="24" cy="179" r="20"/><circle cx="24" cy="256" r="20"/>
      </g>
      <g fill="#fff">
        <polygon points="24,16 33,32 15,32"/>
        <polygon points="24,93 31,101 27,101 27,110 21,110 21,101 17,101"/>
        <rect x="16" y="180" width="3" height="7"/><rect x="22" y="174" width="3" height="13"/><rect x="28" y="170" width="3" height="17"/>
      </g>
      <rect x="23.2" y="20" width="1.6" height="7" fill="var(--red)"/><rect x="23.2" y="28.5" width="1.6" height="1.6" fill="var(--red)"/>
      <path d="M17 256 l5 5 l9 -10" fill="none" stroke="#fff" stroke-width="2.5"/>
    </svg>
    <div class="step" style="left:323px; top:86px;"><div class="head">Lorem Ipsum</div><p>Lorem Ipsum is simply dummy text of the printing and typesetting industry. Lorem Ipsum has been the industry's standard dummy text ever since the 1500s.</p></div>
    <div class="step" style="left:323px; top:162px;"><div class="head">Lorem Ipsum</div><p>Lorem Ipsum is simply dummy text of the printing and typesetting industry. Lorem Ipsum has been the industry's standard dummy text ever since the 1500s.</p></div>
    <div class="step" style="left:323px; top:239px;"><div class="head">Lorem Ipsum</div><p>Lorem Ipsum is simply dummy text of the printing and typesetting industry. Lorem Ipsum has been the industry's standard dummy text ever since the 1500s.</p></div>
    <div class="step" style="left:323px; top:316px;"><div class="head">Lorem Ipsum</div><p>Lorem Ipsum is simply dummy text of the printing and typesetting industry. Lorem Ipsum has been the industry's standard dummy text ever since the 1500s.</p></div>
  </div>
  <div class="page-foot">www.varnstedt-example.fi</div>
  <div class="page-num">04</div>
</section>
<div class="slide-label" style="left:551px; top:1157px;">page 4</div>

</body>
</html>
```